Riverbend Haven Home Care-Nursing Assessment Form

I am creating a Nursing Assessment Form (which is used to be an intake form for all new patients) for my new home care company, Riverbend Haven Home Care.

It is 15 pages and pretty comprehensive as this is a very regulated field. I have all the necessary content and information attached in the word document below. Now, I am seeking a designer to make it look professional, cohesive and easy to read/ follow.
In order for your Word Document Design to be selected, you must:

1. As mentioned previously, make it easy to read/follow. There should be enough spacing, room to write out all necessary notes, fill out check marks...etc...
2. It should look professional.
3. It should be attractive and eye pleasing. Attached you will find our logo-kindly incorporate it's style into the project as well. The logo should be placed on top of each page.
4. Lastly, we need a Word Document version AND PDF Fillable Option. The fillable PDF should Auto Fill for the Name and Start of Care (SOC) Date.

I have attached a sample form below as well. This is how I envision the finished project to look. Of course, I am open to other suggestions as look as it meets the aforementioned requirements.

Thank you! May the best man or woman win!
Our team looks forward to working with our designer on this project!

Industry/Entity Type

Home Health Care

Font styles to use
Sans Serif

Colors
0255a3
9bcb3c

Requirements
Must have
• Refer to Project Description above.
Nice to have
We must be given a Word Document Option and PDF Fillable Option.

```html
<!DOCTYPE html>
<html lang="en">
<head>
<meta charset="utf-8">
<title>Initial Assessment Form – Riverbend Haven Home Care</title>
<link href="https://fonts.googleapis.com/css2?family=Roboto+Condensed:wght@400;700&display=swap" rel="stylesheet">
<style>
  :root{
    --bg:#e9eaec;
    --paper:#ffffff;
    --ink:#1b4592;
    --brand-blue:#0255a3;
    --brand-green:#9bcb3c;
    --green-deep:#8cc63f;
    --green-light:#d4eab0;
    --green-soft:#c6e2a0;
    --row-tint:#f5f9ec;
    --rule:#aab8d6;
  }
  *{box-sizing:border-box;margin:0;padding:0}
  html,body{width:1200px;height:1200px;overflow:hidden}
  body{background:var(--bg);font-family:"Roboto Condensed",sans-serif;color:var(--ink);font-size:12.5px}
  .page{position:absolute;left:190px;top:20px;width:820px;height:1160px;background:var(--paper);box-shadow:0 6px 22px rgba(0,0,0,.18);overflow:hidden}
  .header-art{position:absolute;left:0;top:0;width:820px;height:96px;background:linear-gradient(180deg,var(--green-deep) 0%,var(--brand-green) 45%,var(--green-light) 80%,var(--paper) 100%)}
  .brand{position:absolute;left:48px;top:118px;display:flex;align-items:center;gap:8px}
  .brand-dot{width:14px;height:14px;border-radius:50%;background:var(--brand-green)}
  .brand-name{font-weight:700;font-size:15px;color:var(--brand-blue);text-transform:uppercase;letter-spacing:.2px}
  .form-title{position:absolute;right:50px;top:128px;font-weight:700;font-size:25px;color:var(--brand-blue)}
  .block{position:absolute;left:48px;width:724px}
  .row{position:relative;height:21.5px;line-height:21.5px}
  .row.ruled{border-bottom:1px solid var(--rule)}
  .row.tint{background:var(--row-tint)}
  .row span{position:absolute;top:0;white-space:nowrap}
  .row.center{text-align:center}
  .row.center span{position:static}
  .field-line{display:inline-block;border-bottom:1px dashed var(--ink);height:12px;vertical-align:baseline}
  .band{position:absolute;left:48px;width:726px;height:21px;line-height:21px;background:var(--green-soft);border-radius:4px;text-align:center;font-weight:700;font-size:12.5px;text-transform:uppercase}
  .band.mixed{text-transform:none}
  .opts span{margin:0 14px}
  .rule-only{position:absolute;left:48px;width:724px;border-bottom:1px solid var(--rule)}
</style>
</head>
<body>
<main class="page">
  <div class="header-art" role="img" aria-label="Green decorative header band"></div>

  <div class="brand">
    <span class="brand-dot"></span>
    <span class="brand-name">Riverbend Haven Home Care</span>
  </div>
  <h1 class="form-title">Initial Assessment Form</h1>

  <section class="block" style="top:190px">
    <div class="row">
      <span style="left:0">Name <i class="field-line" style="width:280px"></i></span>
      <span style="left:493px">SOC Date:<i class="field-line" style="width:170px"></i></span>
    </div>
  </section>

  <section class="block" style="top:224px">
    <div class="row ruled tint"><span style="left:7px">Patient’s Name:</span><span style="left:408px">Gender:</span><span style="left:507px">MR#:</span><span style="left:602px">Date:</span></div>
    <div class="row ruled tint"><span style="left:7px">Primary Diagnosis:</span><span style="left:408px">Secondary Diagnosis:</span></div>
    <div class="row ruled tint"><span style="left:7px">Other Pertinent Diagnosis:</span><span style="left:408px">PCP name:</span></div>
    <div class="row ruled tint"><span style="left:7px">Other Physician Name:</span></div>
  </section>

  <section class="block" style="top:332px">
    <div class="row"><span style="left:7px">Prognosis:</span><span style="left:83px">( ) Poor</span><span style="left:178px">( ) Fair</span><span style="left:285px">( ) Good</span><span style="left:392px">( ) Excellent</span></div>
    <div class="row"><span style="left:7px">Vital Signs:</span><span style="left:83px">Height:</span><span style="left:178px">Weight:</span><span style="left:285px">Temp:</span><span style="left:392px">Pulse:</span><span style="left:499px">Resp:</span><span style="left:607px">B/P:</span></div>
    <div class="row ruled"><span style="left:7px">Allergies:</span></div>
    <div class="row ruled" style="margin-top:4px"><span style="left:7px">Past Medical and Surgical History:</span></div>
  </section>
  <div class="rule-only" style="top:436px"></div>

  <div class="band" style="top:448px">Support Systems</div>
  <section class="block" style="top:469px">
    <div class="row center"><span>Married/Not Married/Single/Divorced/Widowed</span></div>
    <div class="row"><span style="left:7px">Lives Alone:&nbsp;&nbsp; ( ) Yes&nbsp;&nbsp; ( ) No</span></div>
    <div class="row ruled"><span style="left:7px">Family Composition:</span></div>
    <div class="row ruled"><span style="left:7px">Past Medical and Surgical History:</span></div>
    <div class="row ruled"><span style="left:7px">Legal Next of Kin:</span><span style="left:511px">Telephone:</span></div>
    <div class="row ruled"><span style="left:7px">Address:</span><span style="left:511px">E-mail:</span></div>
    <div class="row"><span style="left:7px">Is significant other able, available, capable and willing to care for patient?&nbsp; ( ) Yes&nbsp;&nbsp; ( ) No</span></div>
    <div class="row ruled"><span style="left:7px">If No, explain:</span></div>
    <div class="row ruled"><span style="left:7px">Educational Needs of Patient/Family:</span></div>
  </section>

  <div class="band" style="top:677px">Environment</div>
  <section class="block" style="top:699px">
    <div class="row center opts"><span>( ) Private Home</span><span>( ) Apartment</span><span>( ) Elevator</span><span>( ) Walkup</span></div>
  </section>
  <div class="band" style="top:730px"></div>

  <section class="block" style="top:753px">
    <div class="row"><span style="left:7px">( ) Sound structure</span><span style="left:178px">( ) Safe Placement of Cords, Rugs and Furniture</span><span style="left:470px">( ) Adequate Heating and Ventilation</span></div>
    <div class="row"><span style="left:7px">( ) Adequate Cooking facility</span><span style="left:178px">( ) Adequate Plumbing/Sanitation/ Running Water</span><span style="left:470px">( ) Adequate Sleeping Arrangement</span></div>
    <div class="row"><span style="left:7px">( ) Infestations of pests?</span><span style="left:178px">( ) Safe Gas/Electric Appliances</span><span style="left:470px">( ) Enough Electrical Outlets for Equipment</span></div>
    <div class="row"><span style="left:7px">( ) Neighborhood safe?</span><span style="left:178px">( ) Safe storage for Supplies/Equipment/Meds?</span><span style="left:470px">( )&nbsp; Exits Free of Obstruction</span></div>
    <div class="row"><span style="left:7px">( ) Fire extinguisher in home?</span><span style="left:178px">( ) Grounded Plug for Equipment</span><span style="left:470px">( ) Working Telephone in the Home</span></div>
    <div class="row"><span style="left:7px">( ) Working smoke detectors?</span></div>
  </section>

  <div class="band" style="top:893px">Caregiver’s Contact Information</div>
  <section class="block" style="top:914px">
    <div class="row ruled"><span style="left:7px">Name:</span><span style="left:406px">Telephone:</span><span style="left:592px">/</span></div>
    <div class="row ruled"><span style="left:7px">Address:</span><span style="left:406px">Email:</span></div>
    <div class="row ruled"><span style="left:7px">Days / Time Available:</span></div>
  </section>

  <div class="band mixed" style="top:993px">Caregivers Ability to Assist Patient / Able to Provide</div>
  <section class="block" style="top:1014px">
    <div class="row"><span style="left:7px">Personal Care: ( ) Yes ( ) No</span><span style="left:205px">Mobility: ( ) Yes ( ) No</span><span style="left:429px">Prepare/Serve Meals: ( ) Yes ( ) No</span></div>
    <div class="row" style="height:17px;line-height:17px"><span style="left:7px">Maintain Safe/Clean Environment:</span><span style="left:205px">Perform/ Assist with Procedures:</span><span style="left:429px">Caregiver has capacity to learn therapeutic regimen:</span></div>
    <div class="row" style="height:17px;line-height:17px"><span style="left:7px">( ) Yes ( ) No</span><span style="left:205px">( ) Yes ( ) No</span><span style="left:429px">( ) Yes ( ) No</span></div>
    <div class="row ruled"><span style="left:7px">Comments:</span></div>
  </section>
  <div class="rule-only" style="top:1096px"></div>
</main>
</body>
</html>
```